Harlow Vance Civil Construction website design

We want a Bold website to promote our Heavy Civil Construction company, We would like an organic / tangible feel to the site. The pictures will be over saturated so they pop. We need to be able to easliy upload new projects and pictures on a regular basis.
Home page will have a full screen width image, "home page image" with silhouette and logo. It will also have about us area and picture
Page 2 will be Project Gallery with pictures in project folders
Page 3 will be an employment application form and submission
Page 4 will be Contact Us
Construction indusrty
Contractor
Coded - Design and coding required
4 page
- Hypatia Sans Pro Light

```html
<!DOCTYPE html>
<html lang="en">
<head>
<meta charset="utf-8">
<title>Harlow Vance Civil Construction</title>
<link rel="stylesheet" href="https://fonts.googleapis.com/css2?family=Poppins:wght@300;400;500;600;700;800&display=swap">
<style>
:root{
  --blue:#3d55b8;
  --blue-bright:#4a6cf0;
  --ink:#222;
  --grey:#555;
  --muted:#8a8a8a;
  --dark:#232224;
  --panel:#3a8ac0;
  --white:#fff;
}
*{margin:0;padding:0;box-sizing:border-box}
html,body{width:1200px;height:3811px;overflow:hidden}
body{position:relative;background:#fff;font-family:"Poppins",sans-serif;color:var(--ink)}
.abs{position:absolute}

/* header & hero */
.hero{left:0;top:0;width:1200px;height:619px;background:linear-gradient(180deg,#2c5da8 0%,#5f8fcf 40%,#8aa9c9 65%,#b9c3cc 85%,#d6dde5 100%)}
.topbar{left:0;top:27px;width:1003px;height:81px;background:#0d0d0d}
.brand{left:84px;top:44px;display:flex;align-items:center;gap:10px}
.brand-mark{width:40px;height:40px;border:3px solid var(--blue-bright)}
.brand-name{font-weight:600;font-size:17px;line-height:1.15;color:var(--blue-bright);letter-spacing:.5px;width:180px}
.nav{font-size:14px;font-weight:600;color:#fff}
.nav a{color:#fff;text-decoration:none;position:absolute;white-space:nowrap}
.nav a.active{color:#5b7af2}
.hero-frame{left:86px;top:160px;width:222px;height:308px;border:6px solid #d6d6d6;border-right:none}
.hero-frame-r1{left:302px;top:160px;width:6px;height:40px;background:#d6d6d6}
.hero-frame-r2{left:302px;top:420px;width:6px;height:48px;background:#d6d6d6}
.hero-title{left:157px;top:248px;font-size:48px;font-weight:800;line-height:61px;color:#fff;text-transform:uppercase}
.btn-hero{left:158px;top:383px;width:111px;height:37px;background:#fff;border-radius:6px;color:var(--blue);font-size:12px;display:flex;align-items:center;justify-content:center;font-family:Georgia,serif}
.dots{left:1096px;top:248px}

/* features */
.features{left:81px;top:519px;width:1030px;height:218px;background:linear-gradient(180deg,#f6f6f6 0%,#ececec 55%,#d4d4d4 100%)}
.feature{position:absolute;top:34px;width:200px;margin-left:-100px;text-align:center}
.diamond{width:74px;height:74px;margin:0 auto;position:relative}
.diamond::before{content:"";position:absolute;left:11px;top:11px;width:52px;height:52px;background:var(--blue-bright);transform:rotate(45deg)}
.diamond svg{position:absolute;left:22px;top:22px}
.feature p{margin-top:56px;font-size:15px;font-weight:700;color:#444}

/* section headings */
.h2{font-size:31px;font-weight:700;line-height:1;white-space:nowrap}
.h2 .b{color:var(--blue)}
.h2 .g{color:#555}
.bracket{border-left:3px solid var(--blue);border-bottom:3px solid var(--blue)}

/* about */
.about-text{left:81px;top:933px;width:468px}
.about-lead{font-size:17px;font-weight:600;line-height:25px;color:#444;letter-spacing:.8px}
.about-sub{margin-top:8px;font-size:18px;color:#444;letter-spacing:.5px}
.about-body{margin-top:6px;font-size:13.5px;font-weight:300;line-height:21px;color:#666;text-align:justify}
.more{left:81px;top:1170px;display:flex;align-items:center;gap:10px;font-size:12px;font-weight:500;color:#333}
.more span.c{width:38px;height:38px;border-radius:50%;background:#4c5cb4;display:flex;align-items:center;justify-content:center}
.about-img{left:608px;top:876px;width:502px;height:290px;background:linear-gradient(180deg,#9ec4e6 0%,#c7dcec 45%,#7d8f6a 72%,#5c5f4e 100%)}
.about-img-frame{left:622px;top:890px;width:474px;height:264px;border:4px solid #fff}

/* gallery */
.gallery{left:0;top:1332px;width:1200px;height:669px;background:linear-gradient(120deg,#e8e5de 0%,#f1efea 45%,#e2ded4 100%)}
.tile{position:absolute;width:326px;height:197px}
.overlay{position:absolute;left:0;top:0;width:164px;height:197px;background:rgba(74,96,200,.88);color:#fff;font-size:14px;font-weight:600;padding:22px 0 0 32px}

/* review */
.arrow{width:32px;height:30px;border:1px solid #999;display:flex;align-items:center;justify-content:center}
.arrow.on{border-color:var(--blue)}
.review{left:92px;top:2242px;width:501px;height:268px;border:1px solid #cfcfcf}
.avatar{left:29px;top:28px;width:75px;height:78px;background:linear-gradient(180deg,#b9a58d,#6f5a45)}
.reviewer{left:120px;top:66px;font-size:19px;font-weight:500;color:#333}
.reviewer small{display:block;font-size:13px;font-weight:300;color:#999;margin-top:-2px}
.quote{left:46px;top:120px;font-size:64px;font-family:Georgia,serif;color:#c9c9c9;line-height:1}
.review-body{left:97px;top:128px;width:375px;font-size:12px;font-weight:300;line-height:23px;color:#888;text-align:justify}
.clients{left:632px;top:2242px;width:488px;height:265px;display:grid;grid-template-columns:repeat(3,1fr);grid-template-rows:repeat(3,1fr);border:1px solid #ddd}
.clients div{border:1px solid #e2e2e2;display:flex;align-items:center;justify-content:center}
.clients i{width:58px;height:34px;background:#d9d9d9}

/* contact */
.contact{left:0;top:2667px;width:1200px;height:763px;background:var(--dark)}
.info-panel{left:558px;top:2646px;width:642px;height:533px;background:linear-gradient(135deg,#3f8fc6 0%,#3a86bd 50%,#3179ad 100%)}
.form-box{left:67px;top:2775px;width:563px;height:613px;border:4px solid #fff;background:var(--dark)}
.form-title{left:124px;top:2858px;font-size:35px;font-weight:600;color:#fff}
.field{position:absolute;left:127px;width:361px;border-bottom:1px solid #777;font-size:11px;color:#bbb;padding-left:6px;padding-bottom:14px}
.btn-send{left:129px;top:3306px;width:142px;height:54px;border:1px solid #bbb;border-radius:6px;color:#fff;font-size:11px;font-weight:700;display:flex;align-items:center;justify-content:center}
.info{left:713px;color:#fff}
.info .dash{width:14px;height:1px;background:#fff;margin-bottom:16px}
.info h4{font-size:14px;font-weight:600;letter-spacing:.5px}
.info p{font-size:13px;margin-top:16px}
.social{display:flex;gap:18px;margin-top:16px}
.social span{width:20px;height:20px;border:1px solid #3a86bd;border-radius:50%}

/* footer */
.footer{left:0;top:3430px;width:1200px;height:381px;background:#141414}
.f-brand{left:78px;top:3490px;display:flex;align-items:center;gap:10px}
.f-text{left:77px;top:3562px;width:335px;font-size:13px;line-height:19px;color:#ddd;font-weight:300}
.f-h{font-size:20px;font-weight:600;color:#fff;white-space:nowrap}
.f-h::after{content:"";display:block;width:46px;height:2px;background:var(--blue);margin-top:9px}
.f-link{position:absolute;left:470px;font-size:13px;color:#eee}
.f-news{left:678px;top:3562px;width:204px;font-size:12px;line-height:22px;color:#eee;text-align:justify}
.f-input{left:678px;top:3655px;width:203px;height:31px;background:#fff;font-size:10px;color:#333;padding:9px 0 0 12px}
.f-sub{left:678px;top:3719px;width:103px;height:34px;border-radius:17px;background:var(--blue);color:#fff;font-size:11px;font-weight:700;display:flex;align-items:center;justify-content:center}
.thumb{position:absolute;width:56px;height:52px}
</style>
</head>
<body>

<!-- Hero -->
<div class="abs hero" role="img" aria-label="Steel pipe rack structure at an industrial construction site under a blue sky"></div>
<div class="abs topbar"></div>
<div class="abs brand"><span class="brand-mark"></span><span class="brand-name">Harlow Vance Civil Construction</span></div>
<nav class="abs nav" style="left:0;top:58px">
  <a class="active" style="left:589px" href="#">HOME</a>
  <a style="left:665px" href="#">ABOUT US</a>
  <a style="left:770px" href="#">CONTACT US</a>
  <a style="left:891px" href="#">GALLERY</a>
</nav>
<div class="abs hero-frame"></div>
<div class="abs hero-frame-r1"></div>
<div class="abs hero-frame-r2"></div>
<h1 class="abs hero-title">We build your<br>dream</h1>
<div class="abs btn-hero">VIEW MORE</div>
<svg class="abs dots" width="16" height="60" viewBox="0 0 16 60"><circle cx="8" cy="8" r="6" fill="#fff" opacity=".6"/><circle cx="8" cy="42" r="7" fill="none" stroke="#fff" stroke-width="2" opacity=".8"/><circle cx="8" cy="42" r="3" fill="#fff" opacity=".8"/></svg>

<!-- Features -->
<section class="abs features">
  <div class="feature" style="left:193px">
    <div class="diamond"><svg width="30" height="30" viewBox="0 0 30 30" fill="none" stroke="#fff" stroke-width="1.8"><path d="M4 14 L14 5 L24 14"/><path d="M7 12 V25 H16"/><circle cx="21" cy="21" r="5"/><path d="M18.5 21 l2 2 3-4"/></svg></div>
    <p>PERFECT QUALITY</p>
  </div>
  <div class="feature" style="left:412px">
    <div class="diamond"><svg width="30" height="30" viewBox="0 0 30 30" fill="none" stroke="#fff" stroke-width="1.8"><path d="M25 15 a10 10 0 1 1 -4 -8" stroke-dasharray="3 2"/><path d="M21 3 v5 h-5"/><text x="15" y="19" fill="#fff" stroke="none" font-size="10" font-weight="700" text-anchor="middle" font-family="Poppins,sans-serif">24</text></svg></div>
    <p>SUPPORT 24/24</p>
  </div>
  <div class="feature" style="left:629px">
    <div class="diamond"><svg width="30" height="30" viewBox="0 0 30 30" fill="none" stroke="#fff" stroke-width="1.8"><rect x="8" y="4" width="14" height="12"/><path d="M11 8 h8 M11 12 h8"/><rect x="5" y="19" width="20" height="7"/><path d="M9 22.5 h12"/></svg></div>
    <p>MODERN STYLE</p>
  </div>
  <div class="feature" style="left:847px">
    <div class="diamond"><svg width="30" height="30" viewBox="0 0 30 30" fill="none" stroke="#fff" stroke-width="1.8"><path d="M15 3 L26 8 V20 L15 27 L4 20 V8 Z"/><path d="M9 12 L15 9 L21 12 L15 15 Z M9 12 V18 L15 21 V15 M21 12 V18 L15 21"/></svg></div>
    <p>WARRANTY FOREVER</p>
  </div>
</section>

<!-- About -->
<div class="abs bracket" style="left:81px;top:874px;width:114px;height:42px"></div>
<h2 class="abs h2" style="left:101px;top:869px"><span class="g">ABOUT</span> <span class="b">US</span></h2>
<div class="abs about-text">
  <p class="about-lead">Heavy Civil Construction company, has a proud tradition of service as a General Contractor since 2000</p>
  <p class="about-sub">We Offer a Wide Range of Services</p>
  <p class="about-body">Our crews have spent more than two decades moving earth, laying pipe and pouring concrete across the region. Every project begins with careful planning and ends with a site we are proud to hand over. From clearing and grading to final paving, we bring steady hands, heavy equipment and honest schedules to every single job.</p>
</div>
<div class="abs more"><span class="c"><svg width="14" height="10" viewBox="0 0 14 10"><path d="M3 3 L7 7 L11 3" fill="none" stroke="#fff" stroke-width="1.6"/></svg></span>VIEW MORE...</div>
<div class="abs about-img" role="img" aria-label="Long-reach excavator working beside a concrete bridge over water"></div>
<div class="abs about-img-frame"></div>

<!-- Gallery -->
<section class="abs gallery"></section>
<div class="abs bracket" style="left:81px;top:1416px;width:114px;height:42px"></div>
<h2 class="abs h2" style="left:101px;top:1411px"><span class="g">GALLERY</span></h2>
<div class="tile" style="left:81px;top:1490px;background:linear-gradient(135deg,#c9a94a,#6f6a5b)" role="img" aria-label="Yellow drilling rig on a sandy site">
  <div class="overlay">Project Name</div>
</div>
<div class="tile" style="left:434px;top:1490px;background:linear-gradient(160deg,#c2c2b0 0%,#a89377 45%,#7b6149 100%)" role="img" aria-label="Freshly poured curved concrete curb beside graded dirt"></div>
<div class="tile" style="left:786px;top:1490px;background:linear-gradient(135deg,#b4b7bc,#5d6b72 50%,#c4a63a)" role="img" aria-label="Worker in safety vest beside a white utility truck"></div>
<div class="tile" style="left:81px;top:1714px;background:linear-gradient(135deg,#d78a2a,#6b5947 55%,#4f9e8f)" role="img" aria-label="Surveyor working in a trench beside a large green pipe"></div>
<div class="tile" style="left:434px;top:1714px;background:linear-gradient(135deg,#3f7a34,#79a85a 50%,#9aa393)" role="img" aria-label="Aerial view of a new road cutting through green woodland"></div>
<div class="tile" style="left:786px;top:1714px;background:linear-gradient(160deg,#6ea4d6 0%,#d2b75a 45%,#8a6e4f 100%)" role="img" aria-label="Excavators and a worker on a dirt site under blue sky"></div>

<!-- Customer review -->
<div class="abs bracket" style="left:92px;top:2146px;width:150px;height:40px"></div>
<h2 class="abs h2" style="left:115px;top:2136px"><span class="b">CUSTOMER</span> <span class="g">REVIEW</span></h2>
<div class="abs arrow" style="left:516px;top:2155px"><svg width="8" height="12" viewBox="0 0 8 12"><path d="M6 2 L2 6 L6 10" fill="none" stroke="#555" stroke-width="1.5"/></svg></div>
<div class="abs arrow on" style="left:561px;top:2155px"><svg width="8" height="12" viewBox="0 0 8 12"><path d="M2 2 L6 6 L2 10" fill="none" stroke="#3d55b8" stroke-width="1.5"/></svg></div>
<div class="abs review">
  <div class="abs avatar" role="img" aria-label="Customer portrait"></div>
  <div class="abs reviewer">Owen R.<small>CEO</small></div>
  <div class="abs quote">&ldquo;</div>
  <p class="abs review-body">Lorem ipsum dolor sit amet, consectetur adipisicing elit, sed do eiusmod tempor incididunt ut labore et dolore magna aliqua. Ut enim ad minim veniam, quis nostrud exercitation-do eiusmod tempor incididunt ut labore et dolore magna proident.</p>
</div>

<div class="abs bracket" style="left:632px;top:2146px;width:146px;height:40px"></div>
<h2 class="abs h2" style="left:648px;top:2136px"><span class="b">OUR</span> <span class="g">CLIENTS</span></h2>
<div class="abs clients">
  <div><i></i></div><div><i></i></div><div><i></i></div>
  <div><i></i></div><div><i></i></div><div><i></i></div>
  <div><i></i></div><div><i></i></div><div><i></i></div>
</div>

<!-- Contact -->
<section class="abs contact"></section>
<div class="abs info-panel" role="img" aria-label="Blue-tinted aerial map of the service area"></div>
<div class="abs form-box"></div>
<h3 class="abs form-title">Send message <span style="font-weight:400">_</span></h3>
<div class="field" style="top:2947px">Your name</div>
<div class="field" style="top:3012px">Email</div>
<div class="field" style="top:3076px">Reason for inquiry</div>
<div class="field" style="top:3138px;height:94px">Message</div>
<div class="abs btn-send">SEND MESSAGE</div>

<div class="abs info" style="top:2780px"><div class="dash"></div><h4>LOCATION</h4><p>1480 Quarry Road, Ridgefield 3000</p></div>
<div class="abs info" style="top:2888px"><div class="dash"></div><h4>EMAIL</h4><p>hello@harlowvance.com</p></div>
<div class="abs info" style="top:2996px"><div class="dash"></div><h4>PHONE</h4><p>+(00)418 552 0193</p></div>
<div class="abs info" style="top:3196px"><div class="dash"></div><h4 style="color:#3a86bd">CONNECT</h4><div class="social"><span></span><span></span><span></span></div></div>

<!-- Footer -->
<footer class="abs footer"></footer>
<div class="abs f-brand"><span class="brand-mark" style="width:46px;height:46px"></span><span class="brand-name" style="width:200px">Harlow Vance Civil Construction</span></div>
<p class="abs f-text">Lorem ipsum dolor sit amet, consectetur quam justo, pretium adipiscing elit. Vestibulum quam justo, pretium eu tempus ut, ..</p>

<div class="abs f-h" style="left:463px;top:3492px">QUICK LINK</div>
<a class="f-link" style="top:3562px;color:#3d55b8">Home</a>
<a class="f-link" style="top:3614px">About us</a>
<a class="f-link" style="top:3667px">Contact us</a>
<a class="f-link" style="top:3720px">Gallery</a>

<div class="abs f-h" style="left:672px;top:3492px">NEWSLETTER</div>
<p class="abs f-news">Subscribe to this website and receive notifications of new posts by email.</p>
<div class="abs f-input">Email Address</div>
<div class="abs f-sub">SUBSCRIBE</div>

<div class="abs f-h" style="left:981px;top:3492px">GALLERY</div>
<div class="thumb" style="left:984px;top:3565px;background:linear-gradient(135deg,#8fa7bf,#5a6470)" role="img" aria-label="Steel structure thumbnail"></div>
<div class="thumb" style="left:1051px;top:3565px;background:linear-gradient(135deg,#7fb0dc,#b59a3d)" role="img" aria-label="Excavator at bridge thumbnail"></div>
<div class="thumb" style="left:984px;top:3629px;background:linear-gradient(135deg,#a8bcd0,#4f5e6d)" role="img" aria-label="Pipe rack thumbnail"></div>
<div class="thumb" style="left:1051px;top:3629px;background:linear-gradient(135deg,#5f83b8,#b46a3d)" role="img" aria-label="Road at dusk thumbnail"></div>

</body>
</html>
```